Garden building leaflet A4 tri fold

We need an A4 tri fold (printed both sides) flyer design for a local business based in East Hampshire (UK) called Brackwell Yard Buildings.We offer a bespoke garden building service from design, construction, installation and maintenance.Typical use is for home office, garden studio, playrooms, garage workshops, therapy rooms and extra living accommodation. Including connection to all services as required.The final design should stress that this is a local business that has been serving the East Hampshire community for almost 20 years. Over this time Brackwell's has built a reputation for quality construction with customer satisfaction the overriding driving force.Over the last 20 years we've seen a huge increase in people working from home at least one day per week and a shift back to family focused lifestyles. Even large multi national companies are promoting home working as it has been shown by recent studies home workers are more productive than solely office based employees. Brackwell Yard Buildings is a greener way of working, improves work-life balance and accelerates your productivity.

Target Market(s)

ABC1

Industry/Entity Type

Business

Requirements
Must have
• Pictures/photos of garden office buildings and garden studios in typical UK garden surroundings. Contemporary structures essential with modern building design.
Nice to have
• Internal pictures of people working in a garden room or garden studio environment.

```html
<!DOCTYPE html>
<html lang="en">
<head>
<meta charset="utf-8">
<title>Brackwell Yard Buildings – Leaflet</title>
<link href="https://fonts.googleapis.com/css2?family=Roboto:wght@400;500;700;900&family=Roboto+Condensed:wght@500;700&display=swap" rel="stylesheet">
<style>
  :root {
    --leaf: #5cc21a;
    --leaf-light: #9fe04a;
    --leaf-deep: #2e7d12;
    --badge-green: #2f7a0e;
    --lime: #f2f21a;
    --olive: #b7b80e;
    --paper: #ffffff;
    --paper-shade: #ececec;
    --ink: #333333;
    --body: #555555;
    --pill-grey: #e4e4e4;
  }
  * { box-sizing: border-box; margin: 0; padding: 0; }
  html, body { width: 1200px; height: 889px; overflow: hidden; background: #f4f4f4; }
  .leaflet {
    position: relative;
    width: 1200px;
    height: 889px;
    overflow: hidden;
    font-family: "Roboto", Arial, sans-serif;
  }
  .leaflet-shapes { position: absolute; inset: 0; }

  .brand {
    position: absolute;
    left: 830px;
    top: 50px;
    width: 340px;
    text-align: center;
  }
  .brand-name {
    font-family: "Roboto", Arial, sans-serif;
    font-weight: 900;
    font-size: 58px;
    letter-spacing: 1px;
    color: var(--ink);
    line-height: 1;
  }
  .brand-tag {
    display: inline-block;
    margin-top: 28px;
    width: 320px;
    padding: 8px 0 7px;
    border-radius: 24px;
    background: linear-gradient(#f6f6f6, var(--pill-grey));
    font-weight: 500;
    font-size: 27px;
    color: var(--leaf-deep);
    letter-spacing: 0.5px;
  }

  .badge {
    position: absolute;
    left: 903px;
    top: 262px;
    width: 264px;
    height: 264px;
    border-radius: 50%;
    background: var(--paper);
    border: 12px solid var(--lime);
    display: flex;
    flex-direction: column;
    align-items: center;
    justify-content: center;
    font-family: "Roboto Condensed", Arial, sans-serif;
    font-weight: 700;
    line-height: 1.2;
    text-align: center;
  }
  .badge-line { font-size: 31px; color: var(--ink); }
  .badge-area { font-size: 31px; color: var(--badge-green); }
  .badge-years { font-size: 40px; color: var(--badge-green); }

  .side-panel {
    position: absolute;
    left: 0;
    width: 409px;
  }
  .section-title {
    width: 272px;
    height: 37px;
    padding-left: 32px;
    display: flex;
    align-items: center;
    border-radius: 0 20px 20px 0;
    background: linear-gradient(90deg, var(--leaf-light), var(--leaf));
    font-weight: 700;
    font-size: 19px;
    letter-spacing: 0.5px;
    color: #1c2b06;
  }
  .section-text {
    margin: 24px 20px 0 35px;
    font-size: 13.6px;
    line-height: 19.5px;
    color: var(--body);
    text-align: justify;
  }
  .section-text + .section-text { margin-top: 19px; }
  .service { top: 177px; }
  .offer { top: 613px; }

  .call-box {
    position: absolute;
    left: 440px;
    top: 613px;
    width: 331px;
    height: 276px;
    border-radius: 14px 14px 0 0;
    background: rgba(245, 240, 30, 0.88);
    padding-top: 30px;
    text-align: center;
  }
  .call-title {
    display: flex;
    align-items: center;
    justify-content: center;
    gap: 12px;
    font-weight: 500;
    font-size: 34px;
    color: var(--leaf-deep);
  }
  .call-title svg { width: 38px; height: 30px; }
  .call-number {
    font-weight: 700;
    font-size: 36px;
    color: #1a1a1a;
    line-height: 1.2;
    letter-spacing: 1px;
  }
  .call-number:first-of-type { margin-top: 10px; }
</style>
</head>
<body>
<main class="leaflet">
  <svg class="leaflet-shapes" viewBox="0 0 1200 889" width="1200" height="889">
    <defs>
      <linearGradient id="bokehTone" x1="0" y1="0" x2="1" y2="1">
        <stop offset="0" stop-color="#3f9a18"/>
        <stop offset="0.5" stop-color="#6fcf2a"/>
        <stop offset="1" stop-color="#8ee03a"/>
      </linearGradient>
      <linearGradient id="gardenTone" x1="0" y1="0" x2="0" y2="1">
        <stop offset="0" stop-color="#3f6a2c"/>
        <stop offset="0.45" stop-color="#2f5a22"/>
        <stop offset="0.62" stop-color="#6fbf3a"/>
        <stop offset="0.75" stop-color="#9a6a4a"/>
        <stop offset="1" stop-color="#a8583a"/>
      </linearGradient>
      <linearGradient id="paperTone" x1="0" y1="0" x2="1" y2="0">
        <stop offset="0" stop-color="#ffffff"/>
        <stop offset="0.8" stop-color="#fbfbfb"/>
        <stop offset="1" stop-color="var(--paper-shade)"/>
      </linearGradient>
      <clipPath id="belowSwoosh">
        <path d="M0,110 C420,70 900,190 1100,430 C1160,530 1170,700 1172,889 L0,889 Z"/>
      </clipPath>
    </defs>

    <rect width="1200" height="889" fill="url(#bokehTone)" role="img" aria-label="Blurred green foliage backdrop"/>
    <path d="M0,110 C420,70 900,190 1100,430 C1160,530 1170,700 1172,889 L0,889 Z"
          fill="url(#gardenTone)" role="img" aria-label="Photo of a garden patio with deck chairs among tall trees"/>
    <rect x="0" y="0" width="409" height="889" fill="url(#paperTone)" clip-path="url(#belowSwoosh)"/>

    <path d="M0,96 C430,58 920,180 1125,430 C1185,535 1195,700 1198,889"
          fill="none" stroke="var(--olive)" stroke-width="30"/>
    <path d="M0,92 C430,52 915,172 1118,425 C1176,530 1186,700 1188,889"
          fill="none" stroke="var(--lime)" stroke-width="22"/>
    <path d="M0,80 C430,40 910,160 1110,415"
          fill="none" stroke="#ffffff" stroke-opacity="0.6" stroke-width="2"/>
  </svg>

  <header class="brand">
    <h1 class="brand-name">BRACKWELL</h1>
    <p class="brand-tag">YARD BUILDINGS</p>
  </header>

  <div class="badge">
    <span class="badge-line">SERVING</span>
    <span class="badge-area">EAST HAMPSHIRE</span>
    <span class="badge-line">FOR</span>
    <span class="badge-years">20 YEARS</span>
  </div>

  <section class="side-panel service">
    <h2 class="section-title">QUALITY SERVICE</h2>
    <p class="section-text">The service we provide is an end to end solution encompassing the location, the environment, your specific needs for the purpose of the structure, materials that are sympathetic to the locality, the services required and how you envisage your space will look and feel.</p>
    <p class="section-text">Our buildings are exceptional and unrivalled. We source the best quality timber and materials for every stage of our building process right down to the paint systems we use. To this end we are always in the market place ensuring that any improvements in products, techniques and components are implemented by us straight away. We employ skilled craftsmen and a well regarded installation team to finish your building to the very highest of our expected standards.</p>
  </section>

  <section class="side-panel offer">
    <h2 class="section-title">WHAT WE OFFER</h2>
    <p class="section-text">We acknowledge that each customer has individual requirements based on their specific needs and as such we are flexible in our approach to design and installation. We are happy to replicate an existing building from an illustration, picture or even a pencil drawing on a napkin.</p>
    <p class="section-text">Contact us for a no obligation consultation to see how we can make your vision become a reality</p>
  </section>

  <aside class="call-box">
    <p class="call-title">
      <svg viewBox="0 0 38 30" aria-hidden="true">
        <path d="M3,9 C3,3 35,3 35,9 L35,12 L27,12 L27,8 L11,8 L11,12 L3,12 Z" fill="var(--leaf-deep)"/>
        <path d="M12,12 L26,12 L32,26 L6,26 Z" fill="var(--leaf-deep)"/>
        <circle cx="19" cy="19" r="4" fill="var(--lime)"/>
      </svg>
      CALL US
    </p>
    <p class="call-number">01730 555214</p>
    <p class="call-number">07700 900482</p>
  </aside>
</main>
</body>
</html>
```